Business card and stationary design for construction company
RT Garland Construction
Business card and stationary design for construction company - Construction
Creative Brief
Professional
Marcus Garland
President
781 Willow Bend Dr Santa Rosa Beach, FL 32617
marcus@rt-garland.example
rt-garland.example

```html
<!DOCTYPE html>
<html lang="en">
<head>
<meta charset="utf-8">
<title>RT Garland Construction – Business Cards</title>
<link href="https://fonts.googleapis.com/css2?family=Roboto:wght@400;500;700&display=swap" rel="stylesheet">
<style>
  :root {
    --bg: #e6e7ea;
    --navy-deep: #16245a;
    --navy: #1f3479;
    --blue: #2f55b8;
    --white: #ffffff;
    --ink: #1f3479;
    --muted: #c9d3f0;
  }
  * { margin: 0; padding: 0; box-sizing: border-box; }
  html, body { width: 1200px; height: 908px; overflow: hidden; }
  body {
    background: var(--bg);
    font-family: "Roboto", Arial, sans-serif;
    position: relative;
  }
  .card {
    position: absolute;
    left: 250px;
    width: 700px;
    height: 400px;
    border-radius: 28px;
    overflow: hidden;
    box-shadow: 0 10px 24px rgba(0,0,0,0.18);
  }
  .card-front {
    top: 40px;
    background: linear-gradient(135deg, var(--navy-deep) 0%, var(--navy) 55%, var(--blue) 100%);
    color: var(--white);
  }
  .card-back { top: 468px; background: var(--white); }

  .wordmark {
    position: absolute;
    display: flex;
    align-items: center;
    gap: 12px;
    font-weight: 700;
    text-transform: uppercase;
    letter-spacing: 1px;
    line-height: 1.05;
  }
  .wordmark .mark-square { width: 30px; height: 30px; flex: none; }
  .card-front .wordmark { left: 44px; top: 48px; font-size: 30px; color: var(--white); }
  .card-front .wordmark .mark-square { background: var(--white); }
  .decor-square {
    position: absolute; right: 70px; top: 70px;
    width: 230px; height: 230px;
    background: rgba(255,255,255,0.06);
  }
  .services {
    position: absolute; left: 44px; bottom: 48px;
    list-style: none; font-size: 26px; line-height: 1.35;
  }
  .services li::before {
    content: ""; display: inline-block; width: 8px; height: 8px;
    border-radius: 50%; background: var(--white);
    margin-right: 12px; vertical-align: middle;
  }

  .back-band { position: absolute; inset: 0; }
  .card-back .wordmark {
    left: 46px; top: 170px; font-size: 25px; color: var(--ink);
  }
  .card-back .wordmark .mark-square { background: var(--ink); }
  .contact {
    position: absolute; left: 420px; top: 52px;
    list-style: none; color: var(--white); font-size: 15px; line-height: 1.5;
  }
  .contact li { display: flex; align-items: flex-start; gap: 10px; margin-bottom: 6px; }
  .contact svg { width: 18px; height: 18px; flex: none; margin-top: 2px; }
  .person {
    position: absolute; left: 420px; bottom: 52px; color: var(--white);
  }
  .person-name { font-size: 26px; font-weight: 500; }
  .person-title { font-size: 16px; color: var(--muted); margin-top: 4px; }
</style>
</head>
<body>

<section class="card card-front">
  <div class="decor-square"></div>
  <div class="wordmark"><span class="mark-square"></span><span>RT Garland<br>Construction</span></div>
  <ul class="services">
    <li>Commercial</li>
    <li>Industrial</li>
    <li>Residential</li>
  </ul>
</section>

<section class="card card-back">
  <svg class="back-band" viewBox="0 0 700 400" preserveAspectRatio="none">
    <defs>
      <linearGradient id="navyFill" x1="0" y1="0" x2="1" y2="1">
        <stop offset="0" stop-color="#16245a"/>
        <stop offset="1" stop-color="#1f3479"/>
      </linearGradient>
    </defs>
    <path d="M340 0 C 400 120, 400 280, 340 400 L700 400 L700 0 Z" fill="#2f55b8"/>
    <path d="M365 0 C 425 120, 425 280, 365 400 L700 400 L700 0 Z" fill="url(#navyFill)"/>
  </svg>

  <div class="wordmark"><span class="mark-square"></span><span>RT Garland<br>Construction</span></div>

  <ul class="contact">
    <li>
      <svg viewBox="0 0 24 24"><path d="M12 2a7 7 0 0 0-7 7c0 5 7 13 7 13s7-8 7-13a7 7 0 0 0-7-7zm0 9.5A2.5 2.5 0 1 1 12 6.5a2.5 2.5 0 0 1 0 5z" fill="#fff"/></svg>
      <span>781 Willow Bend Dr<br>Santa Rosa Beach, FL 32617</span>
    </li>
    <li>
      <svg viewBox="0 0 24 24"><path d="M6.6 10.8a15 15 0 0 0 6.6 6.6l2.2-2.2a1 1 0 0 1 1-.25 11.4 11.4 0 0 0 3.6.57 1 1 0 0 1 1 1V20a1 1 0 0 1-1 1A17 17 0 0 1 3 4a1 1 0 0 1 1-1h3.5a1 1 0 0 1 1 1c0 1.25.2 2.45.57 3.6a1 1 0 0 1-.25 1z" fill="#fff"/></svg>
      <span>(850) 555-0142</span>
    </li>
    <li>
      <svg viewBox="0 0 24 24"><rect x="3" y="5" width="18" height="14" rx="2" fill="none" stroke="#fff" stroke-width="2"/><path d="M3 7l9 6 9-6" fill="none" stroke="#fff" stroke-width="2"/></svg>
      <span>marcus@rt-garland.example</span>
    </li>
    <li>
      <svg viewBox="0 0 24 24"><circle cx="12" cy="12" r="9" fill="none" stroke="#fff" stroke-width="2"/><path d="M3 12h18M12 3c3 3 3 15 0 18M12 3c-3 3-3 15 0 18" fill="none" stroke="#fff" stroke-width="1.6"/></svg>
      <span>rt-garland.example</span>
    </li>
  </ul>

  <div class="person">
    <div class="person-name">Marcus Garland</div>
    <div class="person-title">President</div>
  </div>
</section>

</body>
</html>
```